Birchfield Elementary School 2019-2020 Priority Goals

This visual will encapsulate our school's annual goals. We are a large elementary school in a high performing school district. We base our annual goals primarily on our school generated set of foundational promises. We know that the relationships of the people are critical to our success. The product will primarily be used with our staff internally to keep focused on our priority goals for the year, which are to innovate and collaborate. The collaboration is both amongst staff and also in stronger partnerships with our parent community. The innovation is in not settling for how things have always been done and will focus in three areas: future ready skills, academic growth and achievement and finally in social/emotional growth. We have been saying to one another that "we will accelerate the academic and social emotional growth of the students we serve by innovating and collaborating.

Target Market(s)

Staff, parents and school board

Industry/Entity Type

Education

Font styles to use
Other font styles liked:
• open to your ideas

Colors
0255a3
fbed22

Requirements
Must have
• pretty new to this idea, we'll attach the early sketches below. You'll also find a school logo design as well as the promises that are referred to in the sketch.
Nice to have
• the colors below are school colors, but we are open to your creative genius as well.

```html
<!DOCTYPE html>
<html lang="en">
<head>
<meta charset="utf-8">
<title>Birchfield Elementary School – 2019-2020 Priority Goals</title>
<link href="https://fonts.googleapis.com/css2?family=Bebas+Neue&family=Oswald:wght@500;600&family=Lato:wght@400;700&family=Gochi+Hand&display=swap" rel="stylesheet">
<style>
  :root{
    --page-bg:#d9dbe0;
    --white:#ffffff;
    --field:#e6e6e6;
    --yellow:#ecc913;
    --stripe-yellow:#f2d21a;
    --mid-blue:#2a78cd;
    --band-blue:#2c7bd0;
    --navy:#27379a;
    --title-navy:#24418f;
    --heart-blue:#74a7e0;
    --accent-blue:#2255c0;
    --footer-navy:#1f3c78;
    --pin-yellow:#f2c40f;
  }
  *{margin:0;padding:0;box-sizing:border-box}
  html,body{width:1200px;height:1200px;overflow:hidden;background:var(--page-bg)}
  .flyer{position:absolute;left:196px;top:30px;width:808px;height:1140px;background:var(--white);overflow:hidden}
  .header-title{position:absolute;left:40px;top:28px;font-family:"Bebas Neue",sans-serif;font-size:46px;color:var(--title-navy);letter-spacing:0.5px;line-height:1}
  .header-title .year{color:var(--band-blue)}
  .mission-band{position:absolute;left:0;top:75px;width:600px;height:98px;background:var(--band-blue)}
  .mission-text{position:absolute;left:42px;top:97px;font-family:"Lato",sans-serif;font-weight:700;font-size:20px;line-height:28px;color:var(--white)}
  .school-name{position:absolute;left:578px;top:30px;width:212px;text-align:center;font-family:"Oswald",sans-serif;font-weight:600;font-size:30px;line-height:1.08;color:var(--title-navy);text-transform:uppercase}
  .school-name .mark{display:block;width:70px;height:70px;margin:0 auto 10px;border-radius:50%;background:var(--stripe-yellow)}
  .field{position:absolute;left:0;top:243px;width:808px;height:798px;background:var(--field)}
  .swirl{position:absolute;left:0;top:0;width:808px;height:1140px}
  .hand{position:absolute;font-family:"Gochi Hand",cursive;color:var(--white);line-height:1;white-space:nowrap}
  .goal{position:absolute;top:566px;font-family:"Bebas Neue",sans-serif;font-size:35px;line-height:1;white-space:nowrap;transform:translateX(-50%)}
  .goal.innovating{left:294px;color:var(--accent-blue)}
  .goal.collaborating{left:491px;color:var(--navy)}
  .plus{position:absolute;left:382px;top:570px;font-family:"Lato",sans-serif;font-weight:700;font-size:24px;color:var(--white);line-height:1;transform:translateX(-50%)}
  .goal-note{position:absolute;top:606px;font-family:"Lato",sans-serif;font-size:15px;line-height:18px;color:var(--white);text-align:center;transform:translateX(-50%);white-space:nowrap}
  .measured{position:absolute;left:405px;top:668px;transform:translateX(-50%);font-family:"Oswald",sans-serif;font-weight:500;font-size:19px;color:var(--navy);line-height:1.1;border-bottom:2px dotted var(--navy);white-space:nowrap;letter-spacing:-0.3px}
  .measures{position:absolute;left:348px;top:700px;list-style:none;font-family:"Lato",sans-serif;font-weight:700;font-size:14.5px;line-height:18.5px;color:var(--white)}
  .measures li{display:flex;align-items:center;gap:6px}
  .measures svg{width:12px;height:12px}
  .closing{position:absolute;left:0;top:968px;width:808px;text-align:center;font-family:"Bebas Neue",sans-serif;font-size:56px;color:var(--title-navy);line-height:1;letter-spacing:0.3px}
  .yellow-stripe{position:absolute;left:0;top:1041px;width:808px;height:15px;background:var(--stripe-yellow)}
  .footer{position:absolute;left:0;top:1056px;width:808px;height:84px;background:var(--footer-navy);font-family:"Lato",sans-serif;font-weight:700;color:var(--white)}
  .contact{position:absolute;display:flex;align-items:center;gap:6px;font-size:16px;line-height:1;white-space:nowrap}
  .contact svg{width:12px;height:14px}
  .social{position:absolute;left:524px;top:28px;display:flex;align-items:center;gap:9px;font-size:21px;white-space:nowrap}
  .social .dot{width:30px;height:30px;border-radius:50%;border:2px solid var(--white);background:var(--band-blue)}
</style>
</head>
<body>
<main class="flyer">
  <h1 class="header-title"><span class="year">2019-2020</span> Priority Goals</h1>
  <div class="mission-band"></div>
  <p class="mission-text">We WILL accelerate the academic, social and<br>emotional growth of the students we serve by:</p>
  <div class="school-name"><span class="mark"></span>Birchfield<br>Elementary School</div>

  <div class="field"></div>

  <svg class="swirl" viewBox="0 0 808 1140" aria-hidden="true">
    <path class="arm-yellow" fill="var(--yellow)" d="M94 760 C50 600 100 330 390 285 C500 268 580 300 605 345 C625 400 640 460 640 525 C610 470 560 440 520 440 C470 440 430 460 403 480 C370 455 300 430 250 450 C180 480 130 560 94 760 Z"/>
    <path class="arm-blue" fill="var(--mid-blue)" stroke="var(--field)" stroke-width="8" stroke-linejoin="round" d="M580 316 C700 370 750 480 745 600 C740 720 700 800 662 834 C600 852 520 834 440 810 C490 775 560 720 595 650 C615 590 612 420 580 316 Z"/>
    <path class="arm-navy" fill="var(--navy)" stroke="var(--field)" stroke-width="8" stroke-linejoin="round" d="M222 495 C140 540 100 640 112 720 C135 870 280 952 420 950 C540 948 630 890 664 838 C600 858 520 842 450 816 L416 812 C360 770 280 710 235 650 C205 600 205 540 222 495 Z"/>
    <path class="heart" fill="var(--heart-blue)" stroke="var(--field)" stroke-width="9" stroke-linejoin="round" d="M400 500 C370 465 310 455 265 478 C210 505 190 570 210 625 C240 700 340 760 416 806 C490 755 575 695 598 625 C620 560 590 475 545 462 C480 445 430 465 400 500 Z"/>
    <g class="icon-bulb" fill="none" stroke="var(--white)" stroke-width="3" stroke-linecap="round">
      <path d="M286 542 C272 532 274 505 298 503 C322 505 324 532 310 542 L308 552 L288 552 Z"/>
      <line x1="290" y1="559" x2="306" y2="559"/>
      <line x1="292" y1="565" x2="304" y2="565"/>
      <line x1="298" y1="490" x2="298" y2="496"/>
      <line x1="274" y1="500" x2="278" y2="504"/>
      <line x1="322" y1="500" x2="318" y2="504"/>
      <line x1="266" y1="522" x2="272" y2="522"/>
      <line x1="324" y1="522" x2="330" y2="522"/>
    </g>
    <g class="icon-people" fill="none" stroke="var(--white)" stroke-width="3" stroke-linejoin="round">
      <circle cx="481" cy="507" r="11"/>
      <circle cx="504" cy="507" r="11"/>
      <path d="M465 558 L465 530 L497 530 L497 558"/>
      <path d="M488 542 L488 530 L520 530 L520 558 L488 558"/>
      <line x1="461" y1="544" x2="524" y2="544"/>
    </g>
  </svg>

  <p class="hand" style="left:208px;top:365px;font-size:26px;line-height:31px">Relationship, Relationships,<br>Relationship</p>
  <span class="goal innovating">Innovating</span>
  <span class="plus">+</span>
  <span class="goal collaborating">Collaborating</span>
  <p class="goal-note" style="left:296px">Agents<br>of Change</p>
  <p class="goal-note" style="left:491px">Staff And Parents<br>Partnership</p>
  <h2 class="measured">MEASURED SUCCESS</h2>
  <ul class="measures">
    <li><svg viewBox="0 0 12 12"><circle cx="6" cy="6" r="5" fill="none" stroke="#fff" stroke-width="1.2"/><path d="M3.5 6 L5.3 7.8 L9.5 3" fill="none" stroke="#fff" stroke-width="1.4"/></svg>Academic</li>
    <li><svg viewBox="0 0 12 12"><circle cx="6" cy="6" r="5" fill="none" stroke="#fff" stroke-width="1.2"/><path d="M3.5 6 L5.3 7.8 L9.5 3" fill="none" stroke="#fff" stroke-width="1.4"/></svg>Social Emotional</li>
    <li><svg viewBox="0 0 12 12"><circle cx="6" cy="6" r="5" fill="none" stroke="#fff" stroke-width="1.2"/><path d="M3.5 6 L5.3 7.8 L9.5 3" fill="none" stroke="#fff" stroke-width="1.4"/></svg>Future Ready</li>
  </ul>
  <p class="hand" style="left:544px;top:728px;font-size:23px;line-height:28px">Finding Every<br>Marla Moment</p>
  <p class="hand" style="left:170px;top:784px;font-size:27px;line-height:33px">Listening<br>&nbsp;&nbsp;&nbsp;&nbsp;for every<br>&nbsp;&nbsp;&nbsp;&nbsp;&nbsp;&nbsp;&nbsp;student’s song</p>

  <h2 class="closing">Foundational Beliefs and Promises</h2>
  <div class="yellow-stripe"></div>
  <footer class="footer">
    <p class="contact" style="left:48px;top:22px"><svg viewBox="0 0 12 14"><path d="M6 13 C2 8 1 6.5 1 5 A5 5 0 0 1 11 5 C11 6.5 10 8 6 13 Z" fill="var(--pin-yellow)"/><circle cx="6" cy="5" r="1.8" fill="var(--footer-navy)"/></svg>1180 Cedar Hollow Rd., Pine Ridge, WA 98400</p>
    <p class="contact" style="left:48px;top:44px"><svg viewBox="0 0 12 14"><path d="M2 2 L4.5 2 L5.5 5 L4 6 C5 8 6 9 8 10 L9 8.5 L12 9.5 L12 12 C6 12 2 8 2 2 Z" fill="var(--pin-yellow)"/></svg>555-210-4400</p>
    <p class="contact" style="left:283px;top:44px"><svg viewBox="0 0 12 14"><rect x="3" y="1" width="6" height="4" fill="var(--pin-yellow)"/><rect x="1" y="5" width="10" height="5" rx="1" fill="var(--pin-yellow)"/><rect x="3" y="9" width="6" height="4" fill="var(--white)"/></svg>555-210-4455</p>
    <p class="social"><span class="dot"></span>@birchfieldleadlearner</p>
  </footer>
</main>
</body>
</html>
```